Anzeigengestaltung für Gebäudedienstleistungsunternehmen
Zielgruppe
Wir sind ein lokales Gebäudedienstleistungsunternehmen und bieten Gebäudereinigung und Haushaltsreinigung, Grünanlagenpflege und Gartenpflege, Winterdienst und Hausmeisterservice für Privat- und Gewerbekunden an.
Aufgabenstellung
Zur Info: Wir benötigen auch ein Flyerdesign. Dieses möchten wir in Anschluss an diesen Auftrag als 1-zu-1 Projekt an den Designer unserer Anzeige vergeben.
Diese Anzeige soll in dem lokalen Mitteilungsblatt (https://www.ost-anzeiger.com/index.php) erscheinen.
Es ist eine farbige zweispaltige (92mm) Anzeige mit der Höhe von 50mm.
Unser Logo und die Firmenfarben sollen verwendet werden. Gerne darf auch ein Foto benutzt werden (z.B. im Hintergrund), welches nach den Jahreszeiten gewechselt werden kann. Zum Beispiel: Frühjahr -> Gartenpflege, Sommer -> Gebäudereinigung, Herbst -> Winterdienst und im Winter -> Hausmeisterservice.
Der Text sollte unsere Dienstleistungen enthalten. Diese sind: Gebäude- und Haushaltsreinigung, Grünanlagen- und Gartenpflege, Winterdienst und Hausmeisterservice. Zusätzlich der Hinweis, dass wir sowohl Privat als auch Gewerbekunden ansprechen möchten.
Unsere Kontaktdaten sollen auch enthalten sein:
Internet: www.wilbeda.de, Telefon: 09847/3318470, E-Mail: kontakt@wilbeda.de
Falls es noch Platz gibt, dann wäre es schön noch den lokalen Bezug herzustellen, indem man die Postleitzahl und den Ort unserer Firma nennt. Eine Nennung der Straße ist nicht vorgesehen.
PLZ: 93418 Ort: Lauf an der Pegnitz od. Lauf a.d. Pegnitz

```html
<!DOCTYPE html>
<html lang="de">
<head>
<meta charset="utf-8">
<title>Wilbeda Gebäudedienste – Anzeige</title>
<link rel="stylesheet" href="https://fonts.googleapis.com/css2?family=Fira+Sans+Condensed:ital,wght@0,400;0,800;1,400&display=swap">
<style>
  :root{
    --brand-blue:#1a5fb4;
    --brand-blue-dark:#0b3f86;
    --brand-blue-light:#3a8fe0;
    --white:#ffffff;
    --photo-green:#4f7a2c;
    --photo-yellow:#d9c766;
    --photo-dark:#1f3a22;
  }
  html,body{margin:0;padding:0;overflow:hidden;background:#fff;}
  .ad{
    position:relative;width:1200px;height:652px;overflow:hidden;
    font-family:"Fira Sans Condensed",Arial,sans-serif;color:var(--white);
  }
  .ad__photo{
    position:absolute;inset:0;
    background:
      radial-gradient(ellipse 40% 55% at 78% 30%, rgba(240,230,150,.85), transparent 70%),
      radial-gradient(ellipse 30% 40% at 95% 10%, rgba(255,250,200,.9), transparent 70%),
      linear-gradient(100deg, var(--photo-dark) 35%, var(--photo-green) 60%, var(--photo-yellow) 85%, #8da04a 100%);
  }
  .ad__overlay{position:absolute;inset:0;width:1200px;height:652px;}
  .brand{
    position:absolute;left:70px;top:58px;display:flex;align-items:center;gap:22px;
  }
  .brand__mark{width:92px;height:92px;background:var(--brand-blue);}
  .brand__name{
    margin:0;font-weight:800;font-size:47px;line-height:48px;letter-spacing:.5px;
    color:var(--brand-blue);text-transform:uppercase;
  }
  .services{
    position:absolute;left:48px;top:218px;margin:0;padding:0;list-style:none;
  }
  .services li{
    font-style:italic;font-size:35px;line-height:54.5px;white-space:nowrap;
  }
  .services li::before{content:"•";margin-right:12px;font-style:normal;}
  .contact{
    position:absolute;left:60px;top:484px;margin:0;padding:0;list-style:none;
  }
  .contact li{
    display:flex;align-items:center;gap:16px;font-size:29px;line-height:38px;
  }
  .contact svg{width:22px;height:22px;flex:none;}
</style>
</head>
<body>
<div class="ad">
  <div class="ad__photo" role="img" aria-label="Foto: Mitarbeiter in Arbeitslatzhose reinigt mit einem Hochdruckreiniger vor sonnigem grünem Garten"></div>

  <svg class="ad__overlay" viewBox="0 0 1200 652" aria-hidden="true">
    <defs>
      <linearGradient id="panelFill" x1="0" y1="0" x2="1" y2="1">
        <stop offset="0" stop-color="#1f6ac0" stop-opacity=".97"/>
        <stop offset=".6" stop-color="#1a5fb4" stop-opacity=".9"/>
        <stop offset="1" stop-color="#3a8fe0" stop-opacity=".55"/>
      </linearGradient>
      <linearGradient id="panelEdge" x1="0" y1="0" x2="1" y2="0">
        <stop offset="0" stop-color="#3a8fe0" stop-opacity=".5"/>
        <stop offset="1" stop-color="#3a8fe0" stop-opacity="0"/>
      </linearGradient>
    </defs>
    <polygon points="0,0 735,0 560,652 0,652" fill="url(#panelFill)"/>
    <polygon points="735,0 800,0 640,652 560,652" fill="url(#panelEdge)"/>
    <polygon class="brand-band" points="0,46 822,46 790,174 0,174" fill="#ffffff"/>
  </svg>

  <div class="brand">
    <div class="brand__mark"></div>
    <p class="brand__name">Wilbeda<br>Gebäudedienste</p>
  </div>

  <ul class="services">
    <li>Gebäude- und Haushaltsreinigung</li>
    <li>Grünanlagen- und Gartenpflege</li>
    <li>Hausmeisterservice</li>
    <li>Winterdienst</li>
  </ul>

  <ul class="contact">
    <li>
      <svg viewBox="0 0 22 22"><rect width="22" height="22" rx="3" fill="#fff"/><circle cx="11" cy="11" r="6.5" fill="none" stroke="#1a5fb4" stroke-width="1.6"/><ellipse cx="11" cy="11" rx="2.8" ry="6.5" fill="none" stroke="#1a5fb4" stroke-width="1.4"/><line x1="4.5" y1="11" x2="17.5" y2="11" stroke="#1a5fb4" stroke-width="1.4"/></svg>
      <span>www.wilbeda.de</span>
    </li>
    <li>
      <svg viewBox="0 0 22 22"><rect width="22" height="22" rx="3" fill="#fff"/><path d="M6 5h3l1.3 3.2-1.7 1.2a8 8 0 0 0 4 4l1.2-1.7L17 13v3a1.5 1.5 0 0 1-1.6 1.5A11 11 0 0 1 4.5 6.6 1.5 1.5 0 0 1 6 5z" fill="#1a5fb4"/></svg>
      <span>09847/3318470</span>
    </li>
    <li>
      <svg viewBox="0 0 22 22"><rect width="22" height="22" rx="3" fill="#fff"/><rect x="4.5" y="6.5" width="13" height="9" fill="none" stroke="#1a5fb4" stroke-width="1.6"/><polyline points="4.5,6.5 11,12 17.5,6.5" fill="none" stroke="#1a5fb4" stroke-width="1.6"/></svg>
      <span>kontakt@wilbeda.de</span>
    </li>
  </ul>
</div>
</body>
</html>
```